Brochure design for TOVANIX clinic

We are seeking for a brochure design for new medical walk-in clinic.
The desirable design for the brochure will contain strong concept of positioning for
" convenience" of medical care in terms of access, affordability and service.
I am looking forward to having eye-catching modern design.
Updates

 I've updated the logo file to ai file

and for your reference please see our web page www.tova-nix.com
to keep consistency in terms of  color scheme  and impression

Thanks

Dear Designers,

We'd like to make the deadline earlier by Dec 17(Tuesday) 
Thank you..

Target Market(s)

Age from 20 - 50

Industry/Entity Type

Medical

Colors
f78f20
33a6d7

Requirements
Must have
• Multi-language greeting line in Korean, Chinese, Japanese and English on the cover page.

8 x11.7 sized tri-fold
Nice to have
• Please refer to our web page in order to keep consistency
www.tova-nix.com

```html
<!DOCTYPE html>
<html lang="en">
<head>
<meta charset="utf-8">
<title>TOVANIX Convenience Clinic – Tri-fold Brochure</title>
<link href="https://fonts.googleapis.com/css2?family=Open+Sans:wght@400;600;700&display=swap" rel="stylesheet">
<style>
:root{
  --orange:#f78f20;
  --blue:#33a6d7;
  --blue-dark:#2b8fbb;
  --grey-dark:#58595b;
  --grey-mid:#4d4d4f;
  --grey-light:#ececec;
  --grey-cell:#e2e2e2;
  --ink:#333;
  --red:#d9393b;
  --page:#ffffff;
}
*{margin:0;padding:0;box-sizing:border-box}
html,body{width:1200px;height:836px;overflow:hidden;background:#fff}
body{font-family:"Open Sans",Arial,sans-serif;color:var(--ink);position:relative}
.spread{position:absolute;top:228px;width:565px;height:380px;background:var(--page);overflow:hidden;box-shadow:0 0 0 1px #ddd}
.spread--outside{left:30px}
.spread--inside{left:605px}
.panel{position:absolute;top:0;height:360px}
.footer{position:absolute;left:0;bottom:0;width:100%;height:20px;background:var(--grey-dark);color:#fff;font-size:6.5px;line-height:20px}
.footer span{position:absolute}
/* outside: info panel */
.info{left:0;width:182px;background:var(--blue);color:#fff}
.info-block{position:absolute;left:10px;width:166px}
.info-icon{position:absolute;left:0;top:0;width:28px;height:28px;background:#fff;border-radius:3px}
.info-icon svg{width:28px;height:28px}
.info-text{margin-left:36px}
.info-text h3{font-size:6.5px;font-weight:700;text-transform:uppercase;margin-bottom:1px}
.info-text ul{list-style:none;font-size:4.8px;line-height:1.3}
.info-text li::before{content:"• "}
/* outside: hours panel */
.hours{left:182px;width:186px;background:var(--grey-light)}
.brand{display:flex;align-items:center;gap:5px;justify-content:center}
.brand-mark{width:14px;height:14px;border:2px solid currentColor}
.brand-name{font-weight:700;letter-spacing:.5px}
.hours .brand{position:absolute;top:28px;width:100%;color:var(--grey-mid);font-size:13px}
.hours .brand-sub,.cover .brand-sub{position:absolute;width:100%;text-align:center;font-size:5px;letter-spacing:1.5px}
.hours .brand-sub{top:48px;color:var(--grey-mid)}
.hours-title{position:absolute;left:20px;top:88px;width:150px;height:23px;background:var(--grey-mid);color:#fff;font-size:9.5px;font-weight:600;display:flex;align-items:center;justify-content:center;gap:5px}
.hours-table{position:absolute;left:20px;top:114px;width:150px;border-collapse:separate;border-spacing:0 2px;font-size:7px}
.hours-table th{background:var(--grey-mid);color:#fff;width:40px;height:16px;font-weight:700}
.hours-table td{background:var(--grey-cell);text-align:center;color:var(--ink)}
.contact{position:absolute;left:0;top:270px;width:186px;height:90px;background:var(--orange);color:#fff;padding:10px 0 0 26px}
.contact-row{display:flex;gap:8px;align-items:flex-start;margin-bottom:7px}
.contact-row svg{width:11px;height:11px;flex:none}
.contact-row small{display:block;font-size:4.5px;text-transform:uppercase;opacity:.9}
.contact-row b{font-size:5.5px;font-weight:600}
/* outside: cover */
.cover{left:368px;width:197px;background:#fff}
.cover .brand{position:absolute;top:16px;width:100%;color:var(--red);font-size:14px}
.cover .brand-sub{top:34px;color:var(--red)}
.cover-photo{position:absolute;left:0;top:50px;width:197px;height:200px;background:linear-gradient(160deg,#eef3f8 0%,#d8e4ee 55%,#c7a893 100%)}
.cover-band{position:absolute;left:20px;top:247px;width:177px;height:22px;background:var(--blue);color:#fff;font-size:10px;padding-left:10px;line-height:22px}
.cover-plus{position:absolute;left:12px;top:244px;width:12px;height:12px;color:#fff}
.greeting{position:absolute;left:0;top:269px;width:197px;height:91px;background:var(--orange);color:#fff;padding:10px 0 0 24px;font-size:10.5px;font-weight:700;line-height:1.32}
/* inside */
.col{font-size:4.4px;line-height:1.35}
.photo{position:absolute;background:linear-gradient(135deg,#f3f6f9,#d9e2ea 60%,#c8b3a3)}
.tab{position:absolute;background:var(--blue);color:#fff;font-size:9px;line-height:18px;padding-left:18px}
.bar{position:absolute;height:10px;background:#8fb9d0;color:#fff;font-size:5px;line-height:10px;padding-left:5px}
.list{position:absolute;list-style:none;font-size:4.4px;line-height:1.35}
.list li::before{content:"• "}
.list h4{font-size:5.4px;font-weight:600;margin-top:2px}
.para{position:absolute;font-size:4.4px;line-height:1.4}
.portrait{position:absolute;background:linear-gradient(160deg,#dfe6ec,#9aa7b3)}
.name{position:absolute;font-size:5px;line-height:1.3;color:var(--orange);font-weight:700}
.name span{display:block;font-weight:600}
</style>
</head>
<body>

<section class="spread spread--outside" aria-label="Brochure outside">
  <div class="panel info">
    <div class="info-block" style="top:12px">
      <div class="info-icon"><svg viewBox="0 0 28 28"><path d="M9 7v7a5 5 0 0 0 10 0V7M14 19v3a3 3 0 0 0 6 0v-2" fill="none" stroke="#33a6d7" stroke-width="1.6"/><circle cx="20" cy="19" r="1.6" fill="#33a6d7"/></svg></div>
      <div class="info-text"><h3>What we do?</h3><ul><li>We provide walk-in healthcare diagnosis and treatment services</li><li>Urgent conditions: fever, skin rash, flu, red eye, simple laceration etc.</li><li>Disease monitoring, screening and general check up</li><li>Prevention and vaccination</li><li>Health education and consultation</li></ul></div>
    </div>
    <div class="info-block" style="top:86px">
      <div class="info-icon"><svg viewBox="0 0 28 28"><rect x="7" y="11" width="14" height="7" rx="3.5" fill="#33a6d7"/><path d="M14 11v7" stroke="#fff" stroke-width="1"/></svg></div>
      <div class="info-text"><h3>How it works</h3><ul><li>Convenient location with ample parking</li><li>Walk-in clinic: no need for appointment or same day appointment at your convenience</li><li>Evening and weekend hours opening (see office hours on home page)</li></ul></div>
    </div>
    <div class="info-block" style="top:164px">
      <div class="info-icon"><svg viewBox="0 0 28 28"><path d="M11 6h6l-1 5 4 7-3 4h-7l-2-4 4-7z" fill="#33a6d7"/><rect x="8" y="21" width="12" height="2" fill="#33a6d7"/></svg></div>
      <div class="info-text"><h3>Why</h3><ul><li>Affordable service</li><li>Easy access and convenient system (Electronic Medical Record and e-Prescription)</li><li>More efficient service</li><li>Evidence-based quality services</li><li>Transparent pricing</li></ul></div>
    </div>
    <div class="info-block" style="top:236px">
      <div class="info-icon"><svg viewBox="0 0 28 28"><rect x="6" y="8" width="16" height="11" fill="none" stroke="#33a6d7" stroke-width="1.6"/><path d="M11 22h6M14 19v3" stroke="#33a6d7" stroke-width="1.6"/></svg></div>
      <div class="info-text"><h3>Now and future</h3><ul><li>We are dedicated to providing under-served populations with health services, with a medical home which is comfortable and efficient, and an environment which offers diverse cultural and medical resources in a variety of languages.</li><li>We pursue continuous innovation and study for better healthcare outcomes and customer convenience.</li></ul></div>
    </div>
  </div>

  <div class="panel hours">
    <div class="brand"><span class="brand-mark"></span><span class="brand-name">TOVANIX</span></div>
    <div class="brand-sub">CONVENIENCE CLINIC</div>
    <div class="hours-title"><svg width="11" height="11" viewBox="0 0 12 12"><circle cx="6" cy="6" r="5" fill="none" stroke="#fff" stroke-width="1.4"/><path d="M6 3v3h2.5" fill="none" stroke="#fff" stroke-width="1.2"/></svg>Office Hours</div>
    <table class="hours-table">
      <tr><th>MON</th><td>9:00am-9:00pm</td></tr>
      <tr><th>TUE</th><td>9:00am-9:00pm</td></tr>
      <tr><th>WED</th><td>9:00am-9:00pm</td></tr>
      <tr><th>THU</th><td>9:00am-9:00pm</td></tr>
      <tr><th>FRI</th><td>9:00am-9:00pm</td></tr>
      <tr><th>SAT</th><td>10:00am-8:00pm</td></tr>
      <tr><th>SUN</th><td>10:00am-8:00pm</td></tr>
    </table>
    <div class="contact">
      <div class="contact-row"><svg viewBox="0 0 12 12"><path d="M6 11S2 6.5 2 4.5a4 4 0 0 1 8 0C10 6.5 6 11 6 11z" fill="#fff"/><circle cx="6" cy="4.5" r="1.4" fill="#f78f20"/></svg><div><small>Where are we?</small><b>1480 Larkspur Ave.<br>Fairview, MI 48190</b></div></div>
      <div class="contact-row"><svg viewBox="0 0 12 12"><circle cx="6" cy="6" r="6" fill="#fff"/><path d="M4 3.2l1 1.6-.6.8a4 4 0 0 0 2 2l.8-.6 1.6 1-.5 1C5.5 9 3 6.5 3 3.7z" fill="#f78f20"/></svg><div><small>Phone</small><b>(555) 014-2290</b></div></div>
      <div class="contact-row"><svg viewBox="0 0 12 12"><circle cx="6" cy="6" r="5.3" fill="none" stroke="#fff" stroke-width="1.2"/><path d="M.8 6h10.4M6 .8c-3 3-3 7.4 0 10.4M6 .8c3 3 3 7.4 0 10.4" fill="none" stroke="#fff" stroke-width=".9"/></svg><div><small>Website</small><b>www.tova-nix.com</b></div></div>
    </div>
  </div>

  <div class="panel cover">
    <div class="brand"><span class="brand-mark"></span><span class="brand-name">TOVANIX</span></div>
    <div class="brand-sub">CONVENIENCE CLINIC</div>
    <div class="cover-photo" role="img" aria-label="Photo of a smiling young woman, clinic patient"></div>
    <div class="cover-band">convenience we value</div>
    <svg class="cover-plus" viewBox="0 0 12 12"><path d="M4 0h4v4h4v4H8v4H4V8H0V4h4z" fill="#fff"/></svg>
    <div class="greeting">Hello<br>Nín Hǎo<br>Kon-nichiwa<br>Annyeonghaseyo</div>
  </div>

  <footer class="footer"><span style="left:48px">www.tova-nix.com</span><span style="left:425px">www.tova-nix.com</span></footer>
</section>

<section class="spread spread--inside" aria-label="Brochure inside">
  <!-- panel 1: services -->
  <div class="photo" style="left:0;top:0;width:188px;height:95px" role="img" aria-label="Photo of a nurse caring for an elderly patient"></div>
  <div class="tab" style="left:14px;top:80px;width:150px">our service</div>
  <p class="para" style="left:12px;top:104px;width:165px">We are dedicated to providing quality healthcare services at an affordable rate, and easy access that is reliable and convenient.</p>
  <div class="bar" style="left:8px;top:122px;width:172px">All Age Group</div>
  <ul class="list" style="left:12px;top:135px;width:82px">
    <h4>Respiratory Conditions</h4><li>Allergies</li><li>Flu</li><li>Sinus Infections</li><li>Sore Throats</li><li>Strep Throat</li><li>Bronchitis</li><li>Colds</li><li>Coughs</li>
    <h4>Head, Ear and Eye</h4><li>Ear aches</li><li>Pink Eye</li><li>Styes</li><li>Ear Infection</li>
  </ul>
  <ul class="list" style="left:98px;top:135px;width:82px">
    <h4>Skin, Hair and Nail</h4><li>Acne</li><li>Poison Ivy</li><li>Sunburn</li><li>Wart Removal</li><li>Insect Bites</li><li>Lice</li><li>Minor Skin Infection and Rashes</li>
    <h4>Digestive and Urinary</h4><li>Bladder Infection</li><li>Diarrhea</li><li>Nausea</li><li>Urinary Tract Infection</li><li>Vomiting</li>
  </ul>
  <div class="bar" style="left:8px;top:254px;width:172px">Adult and Senior</div>
  <ul class="list" style="left:12px;top:268px;width:168px">
    <li>Men's and Women's Diagnostic Screenings (Cholesterol Profile, Liver and Kidney Function Tests and Electrolytes, Prostate Specific Antigen for Men, Thyroid Panel, and many more)</li>
    <li>Heart Health (C-Reactive Protein, Homocysteine, VAP Cholesterol Profile)</li>
    <li>Diabetes Testing (Glucose Screening, Hemoglobin A1c)</li>
    <li>Vaccinations (Flu Shots, Childhood Shots, Adult and Travel Vaccinations)</li>
  </ul>

  <!-- panel 2: experts -->
  <div class="bar" style="left:190px;top:6px;width:120px;background:var(--blue)">Young Adult and Children</div>
  <ul class="list" style="left:196px;top:20px;width:85px"><li>Nutrition Consultation</li><li>Stress Management</li><li>Fatigue Relief</li><li>Back Pain</li></ul>
  <ul class="list" style="left:285px;top:20px;width:85px"><li>Skin Care</li><li>Camp, Sports, School Physicals</li><li>Colds</li><li>Travel Medicine</li></ul>
  <div class="bar" style="left:190px;top:58px;width:80px;background:var(--blue)">Miscellaneous</div>
  <ul class="list" style="left:196px;top:72px;width:85px"><li>B12 Shots</li><li>Ear Irrigation</li><li>Flu Instant Test</li><li>Injectable Antibiotics</li><li>Minor Laceration Closure</li><li>Mono Instant Test</li><li>Nebulizer Breathing Treatments</li><li>Pink Eye Instant Test</li><li>Pregnancy Instant Test</li></ul>
  <ul class="list" style="left:285px;top:72px;width:85px"><li>STD Testing</li><li>Steroid Injections</li><li>Strep Instant Test</li><li>Smoking Cessation</li><li>Suture/Staple Removal</li><li>Throat Culture</li><li>Urinalysis Dipstick</li><li>Urine Drug Screen</li></ul>
  <div class="photo" style="left:196px;top:170px;width:178px;height:86px" role="img" aria-label="Photo of a doctor examining a child with a parent"></div>
  <div class="tab" style="left:204px;top:252px;width:170px">our health experts</div>
  <p class="para" style="left:196px;top:274px;width:176px">We are staffed by specially trained clinicians who provide high quality primary care and can prescribe appropriate medications. They have advanced degrees and clinical training, and work in partnership with outstanding doctors.</p>
  <div class="portrait" style="left:196px;top:306px;width:28px;height:34px" role="img" aria-label="Portrait of the founding director"></div>
  <div class="name" style="left:230px;top:306px">D.K. Harlan, MD, MBA<span>Founder &amp; Managing Director</span></div>
  <p class="para" style="left:230px;top:320px;width:142px">D.K. Harlan, MD, MBA is a trained neurology physician who received an MBA degree and holds clinical experience as a specialist in neurologic disease.</p>

  <!-- panel 3: staff -->
  <p class="para" style="left:380px;top:6px;width:178px">medical school and executive manager as the medical director at Riverside General Hospital. Dr. Harlan has several publications in various neurology journals and consulting experience in healthcare.</p>
  <div class="portrait" style="left:382px;top:38px;width:30px;height:36px" role="img" aria-label="Portrait of the medical director"></div>
  <div class="name" style="left:418px;top:38px">Walter G. Brennick, DO, MS<span>Medical Director</span></div>
  <p class="para" style="left:418px;top:52px;width:142px">Walter G. Brennick, DO, MS received his Doctor of Osteopathy from Northfield University and a Masters Degree in Clinical Research Design and Statistical Analysis from Lakeview State University.</p>
  <p class="para" style="left:382px;top:86px;width:178px">He completed an internship in Detroit and served three years as a general medical officer in the United States Army in southern Europe. He then completed a residency in Emergency Medicine at a university affiliated hospital.</p>
  <p class="para" style="left:382px;top:120px;width:178px">He was an attending Emergency Medicine Physician and an assistant professor in Emergency Medicine. He later took a position at Lakeview State University, where he was active in clinical care, medical education, medical research and research regulatory compliance. His administrative positions have included Associate Chair for Research for the Department of Emergency Medicine and Director of the Office of Human Research Compliance Review in the Office of the Vice-President for Research. In July 2013, Dr. Brennick retired as a professor emeritus.</p>
  <div class="portrait" style="left:382px;top:196px;width:24px;height:28px" role="img" aria-label="Portrait of the nurse practitioner"></div>
  <div class="name" style="left:412px;top:196px">Peter Lindqvist<span>Nurse Practitioner</span></div>
  <p class="para" style="left:412px;top:210px;width:148px">BSN, MSN - Medical Coastal State University; AANP Certified Family Nurse Practitioner</p>
  <div class="name" style="left:382px;top:230px;color:var(--ink)">Nora Castell<span style="font-weight:400">Nurse Practitioner</span></div>
  <div class="name" style="left:382px;top:250px">Mina Seo<span>Administrative Manager</span></div>
  <p class="para" style="left:382px;top:264px;width:178px">Mina Seo has multilingual proficiency of fluent Korean, Chinese and English speaking and writing. Her work experiences include supporting government officials to develop foreign investment, administering at family medicine practice and involving in service industry which needs the highest customer service level.</p>

  <footer class="footer"><span style="left:50px">www.tova-nix.com</span><span style="left:248px">www.tova-nix.com</span><span style="left:440px">www.tova-nix.com</span></footer>
</section>

</body>
</html>
```